BUSINESS CARD - HALVERDINE RURAL SERVICES

I would like to create a business card for my fertilizer spreading business. I would like to incorporate my existing logo and also a description of the services offered. The business card will be given to farmers so must be kept simple but effective. It will also be left in stores so much also be eye catching in order to stand out from other cards.

Target Market(s)

FARMERS

Requirements
Must have
• FRONT OF CARD = EXISTING LOGO + "CUSTOMISED SPREADING" below the logo

REAR Of CARD = SERVICES OFFERED AND CONTACT DETAILS

- Bulk fertilizer including Lime, Gypsum, Manure & Compost
- Granular fertilizer including Single Super, Urea, Gran-am, & Custom Blends
- Modern equipment - Autosteer & Variable Rate Capable
- Friendly & Reliable Service
- Contact Gus: 0471 502 318
Nice to have
• utilize same color scheme as existing logo

```html
<!DOCTYPE html>
<html lang="en">
<head>
<meta charset="utf-8">
<title>Halverdine Rural Services – Business Card</title>
<link href="https://fonts.googleapis.com/css2?family=Lato:wght@400;700&display=swap" rel="stylesheet">
<style>
  :root {
    --page: #ece4d6;
    --card: #ffffff;
    --charcoal: #58585a;
    --orange: #f29a2e;
    --text: #505052;
    --faint: #ececec;
  }
  html, body {
    margin: 0;
    padding: 0;
    width: 1200px;
    height: 1100px;
    overflow: hidden;
    background: var(--page);
    font-family: "Lato", Arial, sans-serif;
  }
  .card {
    position: absolute;
    left: 280px;
    width: 660px;
    height: 377px;
    background: var(--card);
    overflow: hidden;
  }
  .card--front { top: 104px; }
  .card--back { top: 599px; }

  .brand {
    position: absolute;
    left: 0;
    right: 0;
    text-align: center;
    color: var(--charcoal);
    font-weight: 700;
  }
  .brand__mark {
    display: block;
    margin: 0 auto;
    border-radius: 50%;
    background: var(--charcoal);
  }
  .brand__name { display: block; line-height: 1; }
  .brand__sub { display: block; line-height: 1; }

  .card--front .brand { top: 78px; }
  .card--front .brand__mark { width: 136px; height: 136px; margin-bottom: 16px; }
  .card--front .brand__name { font-size: 40px; letter-spacing: -0.5px; }
  .card--front .brand__sub { font-size: 19px; letter-spacing: 4px; margin-top: 6px; }

  .tagline {
    position: absolute;
    left: 0;
    top: 332px;
    width: 660px;
    height: 45px;
  }
  .tagline text {
    font-family: "Lato", Arial, sans-serif;
    font-size: 18px;
    font-weight: 700;
    letter-spacing: 3.5px;
    fill: #ffffff;
  }

  .card--back .brand { top: 30px; }
  .card--back .brand__mark { width: 80px; height: 80px; margin-bottom: 10px; }
  .card--back .brand__name { font-size: 25px; letter-spacing: -0.3px; }
  .card--back .brand__sub { font-size: 12px; letter-spacing: 3px; margin-top: 3px; }

  .watermark {
    position: absolute;
    left: 404px;
    top: 174px;
    width: 168px;
    height: 168px;
    border-radius: 50%;
    background: var(--faint);
  }

  .services {
    position: absolute;
    left: 46px;
    top: 173px;
    margin: 0;
    padding: 0;
    list-style: none;
  }
  .services__item {
    display: flex;
    align-items: center;
    height: 35.4px;
    font-size: 14.5px;
    color: var(--text);
    position: relative;
  }
  .services__icon {
    width: 31px;
    height: 31px;
    flex: none;
  }
  .services__item::after { content: none; }
  .services__bullet {
    width: 5px; height: 5px; border-radius: 50%;
    background: var(--text);
    margin: 0 9px 0 19px;
    flex: none;
  }
</style>
</head>
<body>

<section class="card card--front" aria-label="Card front">
  <div class="brand">
    <span class="brand__mark" aria-hidden="true"></span>
    <span class="brand__name">Halverdine Rural</span>
    <span class="brand__sub">SERVICES</span>
  </div>
  <svg class="tagline" viewBox="0 0 660 45" aria-label="Customised spreading">
    <rect x="0" y="0" width="330" height="45" fill="var(--orange)"/>
    <polygon points="318,0 660,0 660,45 340,45" fill="var(--charcoal)"/>
    <polygon points="314,0 324,0 348,45 338,45" fill="#ffffff"/>
    <text x="173" y="30">CUSTOMISED</text>
    <text x="348" y="30">SPREADING</text>
  </svg>
</section>

<section class="card card--back" aria-label="Card back">
  <div class="watermark" aria-hidden="true"></div>
  <div class="brand">
    <span class="brand__mark" aria-hidden="true"></span>
    <span class="brand__name">Halverdine Rural</span>
    <span class="brand__sub">SERVICES</span>
  </div>

  <ul class="services">
    <li class="services__item">
      <svg class="services__icon" viewBox="0 0 32 32" aria-hidden="true">
        <circle cx="16" cy="16" r="16" fill="var(--orange)"/>
        <path d="M16 7c5 4 5 12 0 18c-5-6-5-14 0-18z" fill="none" stroke="#fff" stroke-width="1.6"/>
        <path d="M16 11v14" stroke="#fff" stroke-width="1.4"/>
      </svg>
      <span class="services__bullet"></span>
      Bulk fertilizer including Lime, Gypsum, Manure &amp; Composts
    </li>
    <li class="services__item">
      <svg class="services__icon" viewBox="0 0 32 32" aria-hidden="true">
        <circle cx="16" cy="16" r="16" fill="var(--orange)"/>
        <path d="M16 23c-6 0-9-4-9-10c5 0 9 4 9 10zM16 23c6 0 9-4 9-10c-5 0-9 4-9 10z" fill="#fff"/>
      </svg>
      <span class="services__bullet"></span>
      Granular fertilizer including Single Super, Urea, Gran-am, &amp; Custom Blends
    </li>
    <li class="services__item">
      <svg class="services__icon" viewBox="0 0 32 32" aria-hidden="true">
        <circle cx="16" cy="16" r="16" fill="var(--orange)"/>
        <path d="M8 16l6 6l11-12" fill="none" stroke="#fff" stroke-width="2.4" stroke-linecap="round" stroke-linejoin="round"/>
      </svg>
      <span class="services__bullet"></span>
      Modern equipment
    </li>
    <li class="services__item">
      <svg class="services__icon" viewBox="0 0 32 32" aria-hidden="true">
        <circle cx="16" cy="16" r="16" fill="var(--orange)"/>
        <circle cx="16" cy="11" r="4" fill="#fff"/>
        <path d="M9 24c0-5 3-8 7-8s7 3 7 8z" fill="#fff"/>
      </svg>
      <span class="services__bullet"></span>
      Friendly &amp; Reliable Service
    </li>
    <li class="services__item">
      <svg class="services__icon" viewBox="0 0 32 32" aria-hidden="true">
        <circle cx="16" cy="16" r="16" fill="var(--orange)"/>
        <path d="M10 8l4 1l1 4l-2 2c1 2 3 4 5 5l2-2l4 1l1 4l-2 2c-7 0-15-8-15-15z" fill="#fff"/>
      </svg>
      <span class="services__bullet"></span>
      Contact Gus: 0471 502 318
    </li>
  </ul>
</section>

</body>
</html>
```